Inspirational quotes poster shop seeks poster designs

Hi! We are launching an eshop with design posterss featuring inspirational quotes. We need a first poster design while looking for further cooperation on around 20 poster designs. We need outputs in the format that can go to high quality print (size at least 100x70cm).

For the first design feel free to choose any of the following quotes to depict:

1. "Stop starting. Start finishing." Author: Torvald Essunger, Klangora
2. "A problem well stated is a problem half solved." Author: Walter P. Brimsley, American inventor
3. "The best way to predict the future is to invent it." Author: Dale Hubbs, Quince

Designs should be rarther simple, think please of your whole concept and how various posters would go together. Every poster can be quite different though, in terms of fonts, colours and overall design, together they should however form and interesting collage.

Designs must contain the quote, author & company. it can be pure text or some indication of the sense of the quote.

Design must also feature company name/logo (not available yet, for now please use "thoughtvolta" as a working name), QR code with a title "Read the story"

See these posters for design we like (for inspiration ONLY!):
http://www.launchtonics.example/products/launch-print-its-simple-until-you-make-it-complicated
http://www.launchtonics.example/products/launch-print-marcus-feldane-less-meetings-more-doing
http://www.launchtonics.example/products/launch-print-gordon-ashfeld-stop-sketching-start-building

Hi to everybody! Sorry for the spam, some of you have been struggling with finding the crux in the quote, so here I offer some ideas what to look for in them. It's up to you to take it, leave it or change it:)

Stop starting, start finishing -
1 - stop starting with many times repeated small word starting, perhaps large word starting made of small words starting, with it contrasting start finishing in normal bold font.
2 - STARTING could look quite unfinished, sketchy, especially -ING could look more unfinished then the rest , e.g. just rough indication of outline of the letters, again contrasting with start finishing will clean & neat writting.

Problem well stated is a problem half solved - look for something that is clearer by defining the problem. Perhaps in a simple sketch like here http://www.launchtonics.example/products/launch-print-its-simple-until-you-make-it-complicated  point out a route from a problem (light = flame), to a solution (lightbulb, lightbulb design drawing or something like that).

Anyway, despite preference for simple design, I am still looking for some smart, creative, catchy idea in the design. Check with yourself if it's something you can would want to buy and hang up on your wall.

Good luck to all of you and again, thank you all very much for participation!
Radim

Target Market(s)

businesses of every size, from startups to large corporates seeking culture change or motivation kick up

Industry/Entity Type

Shop

Requirements
Must have
• I strongly prefer portrait orientation of the poster!

Nice to have
• Quotes themselves are often on the edge, teasing, so the design can be.
Should not have
• Try to avoid traditional dialoge bubble for the quote itself as the first obvious idea for depicting a quote.

Avoid using photos (not simple then) or too many colours.

Of course, by no means use a COPY of existing designs I linked to for inspiration. It just shows what we like.

```html
<!DOCTYPE html>
<html lang="en">
<head>
<meta charset="utf-8">
<title>A problem well stated — thoughtvolta poster</title>
<link href="https://fonts.googleapis.com/css2?family=Ubuntu:wght@500;700&family=Source+Sans+3:wght@300;400&display=swap" rel="stylesheet">
<style>
  :root {
    --page: #ffffff;
    --blue-edge: #1f5fae;
    --blue-mid: #2e72bd;
    --blue-glow: #4d8bcb;
    --ink: #ffffff;
    --muted: #c9d8ec;
    --line: #e6eef8;
    --piece: #eef2f7;
  }
  * { margin: 0; padding: 0; box-sizing: border-box; }
  html, body {
    width: 960px;
    height: 1200px;
    overflow: hidden;
    background: var(--page);
  }
  .poster {
    position: absolute;
    left: 136px;
    top: 22px;
    width: 690px;
    height: 1157px;
    background: radial-gradient(ellipse 60% 50% at 50% 47%, var(--blue-glow) 0%, var(--blue-mid) 60%, var(--blue-edge) 100%);
    color: var(--ink);
    font-family: "Ubuntu", "Fira Sans", sans-serif;
  }
  .emblem {
    position: absolute;
    left: 286px;
    top: 102px;
    width: 124px;
    height: 110px;
    background: linear-gradient(180deg, var(--piece), #dfe6ef);
    opacity: 0.9;
    border-radius: 4px;
  }
  .quote-frame {
    position: absolute;
    left: 50px;
    top: 285px;
    width: 586px;
    height: 586px;
    border: 1.5px solid var(--line);
    border-bottom: none;
  }
  .frame-base {
    position: absolute;
    top: 870px;
    height: 1.5px;
    background: var(--line);
  }
  .frame-base.left { left: 50px; width: 160px; }
  .frame-base.right { left: 476px; width: 160px; }
  .quote {
    position: absolute;
    left: 0;
    width: 100%;
    text-align: center;
    font-weight: 500;
    line-height: 1;
    white-space: nowrap;
  }
  .quote.small { font-size: 55px; }
  .quote.large { font-size: 100px; font-weight: 700; letter-spacing: -0.5px; }
  .line-1 { top: 348px; }
  .line-2 { top: 444px; }
  .line-3 { top: 602px; }
  .line-4 { top: 690px; left: 8px; }
  .author {
    position: absolute;
    left: 0;
    width: 100%;
    top: 855px;
    text-align: center;
    font-family: "Source Sans 3", "Myriad Pro", sans-serif;
    font-weight: 300;
    font-size: 25px;
    color: var(--muted);
  }
  .author-role {
    position: absolute;
    left: 0;
    width: 100%;
    top: 888px;
    text-align: center;
    font-family: "Source Sans 3", "Myriad Pro", sans-serif;
    font-weight: 300;
    font-size: 17px;
    color: var(--muted);
  }
  .brand {
    position: absolute;
    left: 38px;
    top: 1096px;
    font-family: "Source Sans 3", sans-serif;
    font-weight: 400;
    font-size: 17px;
    color: var(--ink);
  }
  .story-link {
    position: absolute;
    right: 36px;
    top: 1096px;
    font-family: "Source Sans 3", sans-serif;
    font-weight: 300;
    font-size: 18px;
    color: var(--muted);
  }
</style>
</head>
<body>
  <main class="poster">
    <div class="emblem" role="img" aria-label="Icon of scattered jigsaw pieces, two of them joined"></div>

    <div class="quote-frame"></div>
    <div class="frame-base left"></div>
    <div class="frame-base right"></div>

    <p class="quote small line-1">A problem</p>
    <p class="quote large line-2">well stated</p>
    <p class="quote small line-3">is a problem</p>
    <p class="quote large line-4">half solved.</p>

    <p class="author">Walter P. Brimsley</p>
    <p class="author-role">American inventor</p>

    <p class="brand">thoughtvolta</p>
    <p class="story-link">Read the story</p>
  </main>
</body>
</html>
```